TALVRO Freightlines #ALLTALVRO Business Cards & Letterhead

I am looking to business cards designed for our organization. We are currently undergoing a small re-branding that is taking place. Our organization is called TALVRO Freightlines and we are headquartered in Phoenix, AZ. We primarily provide transportation and logistics services to the Marrow Parcel Bureau who is our largest customer. I would like to see a design that incorporates name, title, contact info, website, and address (this will be different depending on the employee). I would also like to see some color on the business card using our logo colors or a variation. I would like our logo on the back of the business card with the website displayed. The final design should communicate that we are a next generation transportation operate that focuses on being driver-first, customer-centric, innovative, and sustainable.We would also like our #ALLTALVRO catch phrase incorporated as well.
Updates

Target Market(s)

Transportation & Logistics

Industry/Entity Type

Trucking Company

Contact Information for Business Card

-First and Last Name
-Position Title
-Contact Phone
-Contact Email
-Physical Address

Font styles to use
Serif

Colors

Designer to choose colors to be used in the design.

Requirements
Must have
• -TALVRO logo prominently displayed
• -#ALLTALVRO catch phrase used
• -Some amount of color, design gradient, etc.
• -Logo on the back with website listed (https://www.kavufreightco.example)

```html
<!DOCTYPE html>
<html lang="en">
<head>
<meta charset="utf-8">
<title>TALVRO Freightlines Business Card</title>
<link rel="stylesheet" href="https://fonts.googleapis.com/css2?family=Roboto:wght@400;700;900&family=Roboto+Condensed:wght@400;700&display=swap">
<style>
  :root {
    --brand-green: #84c441;
    --brand-navy: #0d3a4a;
    --ink-gray: #5a5a5a;
    --divider-gray: #c9c9c9;
    --paper: #ffffff;
    --backdrop: #7a7a7a;
  }
  * { box-sizing: border-box; margin: 0; padding: 0; }
  html, body {
    width: 1200px; height: 675px; overflow: hidden;
    background: var(--backdrop);
    font-family: "Roboto", Arial, sans-serif;
  }
  .stage { position: relative; width: 1200px; height: 675px; }
  .card {
    position: absolute; top: 183px;
    width: 540px; height: 309px;
    border-radius: 16px; overflow: hidden;
    box-shadow: 0 6px 18px rgba(0,0,0,0.35);
  }
  /* Back side */
  .card-back { left: 40px; background: var(--brand-green); color: var(--paper); }
  .card-back .brand-mark {
    position: absolute; left: 0; right: 0; top: 112px;
    display: flex; justify-content: center; align-items: center; gap: 14px;
  }
  .card-back .brand-dot { width: 20px; height: 20px; border-radius: 50%; background: var(--paper); }
  .card-back .brand-name { font-weight: 900; font-size: 52px; letter-spacing: 1px; color: var(--paper); }
  .card-back .website {
    position: absolute; left: 0; right: 0; bottom: 36px;
    text-align: center; font-size: 15px; letter-spacing: 0.3px;
  }
  /* Front side */
  .card-front { left: 620px; background: var(--paper); }
  .identity {
    position: absolute; left: 20px; top: 84px; width: 264px;
    text-align: center;
  }
  .identity .brand-mark { display: flex; justify-content: center; align-items: center; gap: 12px; }
  .identity .brand-dot { width: 18px; height: 18px; border-radius: 50%; background: var(--brand-green); }
  .identity .brand-name { font-weight: 900; font-size: 48px; color: var(--brand-navy); letter-spacing: 1px; }
  .identity .tagline {
    margin-top: 12px; white-space: nowrap;
    font-family: "Roboto Condensed", Arial, sans-serif;
    font-size: 16px; color: var(--brand-green);
  }
  .divider {
    position: absolute; left: 296px; top: 52px;
    width: 1px; height: 150px;
    background: linear-gradient(to bottom, transparent, var(--divider-gray) 20%, var(--divider-gray) 80%, transparent);
  }
  .contact {
    position: absolute; left: 314px; top: 52px; width: 215px;
    color: var(--ink-gray); font-size: 12px; line-height: 1.45;
  }
  .contact .person-name { font-weight: 900; font-size: 19px; color: var(--brand-navy); line-height: 1.1; }
  .contact .person-title { color: var(--brand-green); font-size: 13px; margin-bottom: 8px; }
  .contact .address { margin-bottom: 8px; }
  .contact .line { display: flex; align-items: center; gap: 6px; white-space: nowrap; }
  .contact .line svg { width: 11px; height: 11px; flex: none; }
  .footer-band {
    position: absolute; left: 0; right: 0; bottom: 0; height: 52px;
    background: var(--brand-green);
    border-top: 4px solid var(--brand-navy);
    display: flex; align-items: center; justify-content: center;
  }
  .footer-band .hashtag {
    color: var(--paper); font-weight: 700; font-size: 17px; letter-spacing: 0.5px;
    margin-left: 120px;
  }
</style>
</head>
<body>
<main class="stage">
  <section class="card card-back">
    <div class="brand-mark">
      <span class="brand-dot"></span>
      <span class="brand-name">TALVRO</span>
    </div>
    <p class="website">www.talvrofreight.example</p>
  </section>

  <section class="card card-front">
    <div class="identity">
      <div class="brand-mark">
        <span class="brand-dot"></span>
        <span class="brand-name">TALVRO</span>
      </div>
      <p class="tagline">Transportation and Logistics Services</p>
    </div>

    <div class="divider"></div>

    <div class="contact">
      <p class="person-name">JORDAN VALE</p>
      <p class="person-title">President</p>
      <p class="address">4120 West Saguaro Ridge Road<br>Glendale, AZ 85301</p>
      <p class="line">
        <svg viewBox="0 0 12 12" aria-hidden="true"><path fill="var(--brand-green)" d="M2.5 1l2 2.3-1 1.2a7 7 0 0 0 4 4l1.2-1 2.3 2-1.2 1.5C5.5 11 1 6.5.9 2.2z"/></svg>
        555-014-2291
      </p>
      <p class="line">
        <svg viewBox="0 0 12 12" aria-hidden="true"><rect x="0.5" y="2" width="11" height="8" fill="var(--brand-green)"/><path d="M0.5 2l5.5 4.5L11.5 2" fill="none" stroke="#fff" stroke-width="1"/></svg>
        info@talvrofreight.example
      </p>
      <p class="line">
        <svg viewBox="0 0 12 12" aria-hidden="true"><circle cx="6" cy="6" r="5.2" fill="none" stroke="var(--brand-green)" stroke-width="1.2"/><path d="M1 6h10M6 1c-2.5 3-2.5 7 0 10M6 1c2.5 3 2.5 7 0 10" fill="none" stroke="var(--brand-green)" stroke-width="0.9"/></svg>
        www.talvrofreight.example
      </p>
    </div>

    <div class="footer-band">
      <span class="hashtag">#ALLTALVRO</span>
    </div>
  </section>
</main>
</body>
</html>
```